Brightvale Solutions company needs a homepage design

We need a homepage designed for a new company based in Des Moines, IA called Go Brightvale Solutions. They sell Carewell Supplement plans to seniors. The design should communicate trust, security, be vibrant and easy to read with larger font and clear messages. The goal for visitors is to ultimately get a free quote and purchase a plan after a call from a licensed agent.

```html
<!DOCTYPE html>
<html lang="en">
<head>
<meta charset="utf-8">
<title>Go Brightvale Solutions – Home</title>
<link href="https://fonts.googleapis.com/css2?family=Poppins:wght@300;400;500;600;700&display=swap" rel="stylesheet">
<style>
:root{
  --brand:#3d97e6;
  --sky:#7fbef8;
  --sky-title:#6cb4f0;
  --ink:#1b1b1b;
  --grey-head:#8c8c8c;
  --text:#6e6e6e;
  --muted:#9a9a9a;
  --line:#e6e6e6;
  --white:#ffffff;
  --band-dark:#4a6887;
}
*{margin:0;padding:0;box-sizing:border-box}
html,body{width:1200px;height:3051px;overflow:hidden;background:var(--white)}
body{font-family:'Poppins',sans-serif;color:var(--text);position:relative}
.abs{position:absolute}

/* header */
.logo{display:flex;align-items:center;gap:12px}
.logo-mark{width:58px;height:54px;border-radius:9px;background:var(--sky)}
.logo-name{font-size:25px;font-weight:500;color:var(--brand);white-space:nowrap}
.site-header .logo{left:152px;top:48px}
.nav{top:68px;left:0;width:1200px;height:30px}
.nav a{position:absolute;font-size:13.5px;font-weight:500;color:var(--ink);text-decoration:none;white-space:nowrap}
.nav a.active::after{content:"";position:absolute;left:0;right:0;bottom:-14px;height:3px;background:var(--sky)}

/* hero */
.hero-photo{left:0;top:120px;width:1000px;height:500px;
  background:linear-gradient(90deg,#9e9e9e 0%,#c4c4c4 35%,#dedede 55%,#f4f4f4 78%,#ffffff 100%)}
.hero-title{left:600px;top:214px;font-size:42px;line-height:44px;font-weight:600;color:var(--grey-head)}
.zip{left:600px;top:382px;width:410px;height:49px;background:#f5f5f5;font-size:11px;color:#aaa;padding:18px 18px}
.btn{display:flex;align-items:center;justify-content:center;background:var(--sky);color:var(--white);font-weight:600;font-size:18px;border-radius:3px}
.hero .btn{left:600px;top:448px;width:215px;height:52px}
.fine{font-size:8.5px;color:#9a9a9a;white-space:nowrap}
.hero .fine{left:614px;top:510px}
.dots{left:1150px;top:316px;width:10px}
.dots span{display:block;width:9px;height:9px;border-radius:50%;background:#d8d8d8;margin-bottom:19px}
.dots span.on{background:var(--sky)}

/* welcome */
.section-title{font-size:24px;font-weight:600}
.welcome .section-title{left:199px;top:720px;color:var(--sky-title)}
.welcome p{left:199px;top:790px;width:462px;font-size:14px;line-height:29.5px;color:var(--text)}
.read-more{left:199px;top:975px;font-size:13px;font-weight:600;color:var(--sky-title)}
.welcome-photo{left:675px;top:740px;width:322px;height:251px;background:linear-gradient(135deg,#b8a48e,#d7c6b2 55%,#e9ded0)}

/* services */
.services{left:0;top:1090px;width:1200px;height:321px;background:var(--sky)}
.services .section-title{left:0;width:1200px;top:54px;text-align:center;color:var(--white)}
.service{top:148px;width:260px}
.service h3{display:flex;align-items:center;gap:12px;font-size:13px;font-weight:500;color:var(--white);height:30px}
.service p{margin-top:12px;font-size:11px;line-height:23px;color:#eaf4fe}

/* what is */
.what{left:0;top:1411px;width:1200px;height:444px;background:linear-gradient(90deg,#3e5a78,#5f7e9e 50%,#3e5a78)}
.what .section-title{left:0;width:1200px;top:106px;text-align:center;color:var(--white)}
.what p{left:200px;top:178px;width:800px;text-align:center;font-size:11px;line-height:24px;color:#e6edf5}
.what .btn{left:492px;top:298px;width:216px;height:52px}
.what .fine{left:0;width:1200px;text-align:center;top:361px;color:#d5e0ec}

/* how it works */
.how .section-title{left:0;width:1200px;top:1916px;text-align:center;color:var(--ink)}
.video-frame{left:279px;top:1989px;width:640px;height:320px;background:#ececec;padding:8px}
.video{width:100%;height:100%;background:linear-gradient(160deg,#9cb3c9,#d9d0c0 50%,#8a7a62);position:relative}
.play{position:absolute;left:50%;top:50%;transform:translate(-50%,-50%)}

/* testimonials */
.testimonials{left:0;top:2360px;width:1200px;height:480px;background:#fafafa}
.testimonials .section-title{left:0;width:1200px;top:108px;text-align:center;color:var(--sky-title)}
.quote{top:197px;width:420px}
.avatar{position:absolute;left:0;top:0;width:120px;height:120px;border-radius:50%;border:4px solid var(--sky);background:linear-gradient(135deg,#c9b39a,#e4d8c8)}
.quote-body{position:absolute;left:141px;top:8px;width:220px}
.quote-body h4{font-size:17px;font-weight:600;color:var(--ink)}
.quote-body .company{font-size:12px;color:var(--muted)}
.quote-body .rule{width:44px;height:3px;background:var(--sky);margin:12px 0 14px}
.quote-body p{font-size:11px;line-height:22.5px;color:var(--text)}
.arrows{left:580px;top:2425px;top:425px;display:flex;gap:10px}

/* footer */
.site-footer .logo{left:433px;top:2900px}
.copy{left:0;width:1200px;top:2978px;text-align:center;font-size:13px;color:var(--ink)}
</style>
</head>
<body>

<header class="site-header">
  <div class="abs logo"><span class="logo-mark"></span><span class="logo-name">Go Brightvale Solutions</span></div>
  <nav class="abs nav">
    <a class="active" style="left:555px">Home</a>
    <a style="left:643px">About Us</a>
    <a style="left:749px">Services</a>
    <a style="left:852px">FAQ's</a>
    <a style="left:934px">Contact Us</a>
  </nav>
</header>

<section class="hero">
  <div class="abs hero-photo" role="img" aria-label="Black and white photo of a smiling senior couple"></div>
  <h1 class="abs hero-title">We sell Carewell<br>Supplement<br>plans to seniors</h1>
  <div class="abs zip">Enter Your Zip Code Now</div>
  <a class="abs btn">Get A Free Quote</a>
  <div class="abs fine">Purchase a plan after a call from a licensed agent.</div>
  <div class="abs dots"><span></span><span></span><span></span><span class="on"></span></div>
</section>

<section class="welcome">
  <h2 class="abs section-title">Welcome to Brightvale Solutions</h2>
  <p class="abs">At vero eos et accusamus et iusto odio dignissimos ducimus qui blanditiis praesentium voluptatum deleniti atque corrupti quos dolores et quas molestias excepturi sint occaecati cupiditate non provident, similique sunt in culpa qui officia deserunt mollitia animi, id est laborum et dolorum fuga. Et harum quidem rerum facilis est et expedita distinctio. Nam libero tempore.</p>
  <a class="abs read-more">Read More &gt;&gt;</a>
  <div class="abs welcome-photo" role="img" aria-label="Photo of a happy senior couple at home"></div>
</section>

<section class="abs services">
  <h2 class="abs section-title">Our Supplement Services</h2>
  <div class="abs service" style="left:199px">
    <h3><svg width="34" height="24" viewBox="0 0 34 24"><rect x="1" y="5" width="32" height="18" rx="3" fill="#3d86d6"/><rect x="12" y="1" width="10" height="5" rx="1" fill="none" stroke="#3d86d6" stroke-width="2"/><path d="M17 9v10M12 14h10" stroke="#fff" stroke-width="2.4"/></svg>Hospital Insurance</h3>
    <p>At vero eos et accusamus et iusto odio dignissimos ducimus qui blanditiis praesentium voluptatum deleniti atque corrupti</p>
  </div>
  <div class="abs service" style="left:472px">
    <h3><svg width="40" height="24" viewBox="0 0 40 24"><path d="M1 13h10l3-8 5 16 4-12 3 4h13" fill="none" stroke="#fff" stroke-width="2"/></svg>Medical Insurance</h3>
    <p>At vero eos et accusamus et iusto odio dignissimos ducimus qui blanditiis praesentium voluptatum deleniti atque corrupti</p>
  </div>
  <div class="abs service" style="left:746px">
    <h3><svg width="24" height="26" viewBox="0 0 24 26"><circle cx="11" cy="3" r="2.5" fill="#fff"/><path d="M11 7v8h7l3 7M8 11a7 7 0 1 0 9 10" fill="none" stroke="#fff" stroke-width="2"/></svg>Carewell Advantage</h3>
    <p>At vero eos et accusamus et iusto odio dignissimos ducimus qui blanditiis praesentium voluptatum deleniti atque corrupti</p>
  </div>
</section>

<section class="abs what" role="img" aria-label="Blue-tinted photo of a smiling senior couple">
  <h2 class="abs section-title">What is Carewell Supplement</h2>
  <p class="abs">At vero eos et accusamus et iusto odio dignissimos ducimus qui blanditiis praesentium voluptatum deleniti atque corrupti quos dolores et quas molestias excepturi sint occaecati cupiditate non provident, similique sunt in culpa qui officia deserunt mollitia animi, id est laborum et dolorum fuga. Et harum quidem rerum facilis est et expedita distinctio. Nam libero tempore, cum soluta nobis est eligendi</p>
  <a class="abs btn">Get A Free Quote</a>
  <div class="abs fine">Purchase a plan after a call from a licensed agent.</div>
</section>

<section class="how">
  <h2 class="abs section-title">How It Works</h2>
  <div class="abs video-frame">
    <div class="video" role="img" aria-label="Video still of a senior couple outdoors beside a tree">
      <svg class="play" width="66" height="66" viewBox="0 0 66 66"><circle cx="33" cy="33" r="30" fill="rgba(255,255,255,.25)" stroke="#fff" stroke-width="3"/><path d="M27 21l18 12-18 12z" fill="#fff"/></svg>
    </div>
  </div>
</section>

<section class="abs testimonials">
  <h2 class="abs section-title">Testimonials</h2>
  <div class="abs quote" style="left:201px">
    <div class="avatar" role="img" aria-label="Portrait of a customer"></div>
    <div class="quote-body">
      <h4>Daniel Harper</h4><div class="company">Company Name</div><div class="rule"></div>
      <p>At vero eos et accusamus et iusto odio dignissimos ducimus qui blanditiis praesentium voluptatum deleniti atque corrupti quos dolores et quas molestias excepturi sint occaecati</p>
    </div>
  </div>
  <div class="abs quote" style="left:606px">
    <div class="avatar" role="img" aria-label="Portrait of a customer"></div>
    <div class="quote-body">
      <h4>Daniel Harper</h4><div class="company">Company Name</div><div class="rule"></div>
      <p>At vero eos et accusamus et iusto odio dignissimos ducimus qui blanditiis praesentium voluptatum deleniti atque corrupti quos dolores et quas molestias excepturi sint occaecati</p>
    </div>
  </div>
  <div class="abs arrows">
    <svg width="12" height="16" viewBox="0 0 12 16"><path d="M9 2L3 8l6 6" fill="none" stroke="#111" stroke-width="2.4"/></svg>
    <svg width="12" height="16" viewBox="0 0 12 16"><path d="M3 2l6 6-6 6" fill="none" stroke="#111" stroke-width="2.4"/></svg>
  </div>
</section>

<footer class="site-footer">
  <div class="abs logo"><span class="logo-mark"></span><span class="logo-name">Go Brightvale Solutions</span></div>
  <div class="abs copy">© 2017 Company Name &nbsp;|&nbsp; All Rights Reserved</div>
</footer>

</body>
</html>
```